Lawn Care business truck wrap

I am needing a truck wrap for a Regular Cab 2015 Vexor 2700. The truck is currently blue but I want the base of the wrap to be white as if it were on a white truck. Ive uploaded two images, one of my logo and another of the color ideas I have for the truck. I'm not wanting the "Landscape Maintenance" part of the logo on the wrap. Lastly the phone number is 406-315-7084. A list of services that we provide are: Weekly Lawn maintenance, Sprinkler Repairs, Fertilizing and Weed Control.

Target Market(s)

Residential home owners

Industry/Entity Type

Landscape

Colors
fbed22
9bcb3c
acd037
fbee3d

Requirements
Must have
• Logo, Phone Number, list of services provided
Nice to have
• A catchy design that is easily recognized on the road.
Should not have
• The tailgate of the truck will not be there so no graphics on the tailgate.

```html
<!DOCTYPE html>
<html lang="en">
<head>
<meta charset="utf-8">
<title>Verdano Lawn Care – Truck Wrap Layouts</title>
<link rel="stylesheet" href="https://fonts.googleapis.com/css2?family=Oswald:wght@500;600&display=swap">
<style>
  :root {
    --wrap-yellow: #dcd31f;
    --forest: #0d4a34;
    --phone-green: #2f8a48;
    --glass: #dcdedf;
    --tire: #1d1d1d;
    --rim: #9a9a9a;
    --trim: #222;
    --page: #ffffff;
  }
  html, body {
    margin: 0;
    width: 1200px;
    height: 1200px;
    overflow: hidden;
    background: var(--page);
  }
  .wrap-sheet { display: block; width: 1200px; height: 1200px; }
  .body-panel { fill: var(--wrap-yellow); }
  .glass { fill: var(--glass); }
  .trim { fill: var(--trim); }
  .tire { fill: var(--tire); }
  .rim { fill: var(--rim); }
  .forest-band { fill: var(--forest); }
  .grass-field { fill: url(#grassTone); }
  .accent-stripe { fill: var(--forest); }
  .brand-name {
    font-family: "Oswald", sans-serif;
    font-weight: 500;
    fill: var(--forest);
    letter-spacing: 2px;
  }
  .phone {
    font-family: "Oswald", sans-serif;
    font-weight: 600;
    letter-spacing: 2px;
  }
  .phone--dark { fill: var(--forest); }
  .phone--green { fill: var(--phone-green); }
  .services {
    font-family: "Oswald", sans-serif;
    font-weight: 600;
    font-size: 11px;
    letter-spacing: 0.3px;
  }
  .services--light { fill: #ffffff; }
  .services--dark { fill: var(--forest); }
</style>
</head>
<body>
<svg class="wrap-sheet" viewBox="0 0 960 960" xmlns="http://www.w3.org/2000/svg">
  <defs>
    <linearGradient id="grassTone" x1="0" y1="0" x2="0" y2="1">
      <stop offset="0" stop-color="#1f6e33"/>
      <stop offset="1" stop-color="#3d9a3a"/>
    </linearGradient>
    <linearGradient id="sheen" x1="0" y1="0" x2="0" y2="1">
      <stop offset="0" stop-color="#ece42a"/>
      <stop offset="1" stop-color="#d2c81c"/>
    </linearGradient>
    <clipPath id="bodyClip">
      <path d="M45,240 L62,224 L235,200 L345,135 L485,127 L500,205 L905,200 L913,340 L805,345 A75,75 0 0 0 655,350 L245,358 A75,75 0 0 0 95,350 L45,345 Z"/>
    </clipPath>
    <g id="truckBody">
      <path class="body-panel" fill="url(#sheen)" d="M45,240 L62,224 L235,200 L345,135 L485,127 L500,205 L905,200 L913,340 L805,345 A75,75 0 0 0 655,350 L245,358 A75,75 0 0 0 95,350 L45,345 Z"/>
      <path class="glass" d="M300,185 L360,143 L445,140 L450,205 L300,208 Z"/>
      <rect class="trim" x="500" y="198" width="408" height="6"/>
      <rect class="trim" x="36" y="300" width="30" height="45" rx="4"/>
      <rect class="trim" x="865" y="300" width="58" height="40" rx="4"/>
      <circle class="tire" cx="170" cy="370" r="64"/>
      <circle class="rim" cx="170" cy="370" r="38"/>
      <circle class="tire" cx="730" cy="372" r="64"/>
      <circle class="rim" cx="730" cy="372" r="38"/>
    </g>
  </defs>

  <!-- Layout A: bold name, services on band -->
  <g class="layout layout--a">
    <use href="#truckBody"/>
    <g clip-path="url(#bodyClip)">
      <polygon class="accent-stripe" points="85,262 500,214 500,220 85,270"/>
      <polygon class="forest-band" points="255,330 640,324 910,262 920,400 255,400"/>
      <polygon class="grass-field" role="img" aria-label="Grass blade illustration along lower body"
               points="255,356 640,348 910,282 920,400 255,400"/>
    </g>
    <text class="brand-name" x="262" y="316" font-size="72" textLength="370" lengthAdjust="spacingAndGlyphs">VERDANO</text>
    <text class="phone phone--dark" x="683" y="258" font-size="25" textLength="175" lengthAdjust="spacingAndGlyphs">406-315-7084</text>
    <text class="services services--light" x="264" y="345" transform="rotate(-1 264 345)" textLength="366" lengthAdjust="spacingAndGlyphs">WEEKLY LAWN MAINTENANCE | SPRINKLER REPAIRS | FERTILIZING | WEED CONTROL</text>
  </g>

  <!-- Layout B: compact name, services above band -->
  <g class="layout layout--b" transform="translate(0,440)">
    <use href="#truckBody"/>
    <g clip-path="url(#bodyClip)">
      <polygon class="accent-stripe" points="85,272 500,222 500,228 85,280"/>
      <polygon class="forest-band" points="255,340 500,333 910,262 920,400 255,400"/>
      <polygon class="grass-field" role="img" aria-label="Grass blade illustration along lower body"
               points="255,348 500,341 910,272 920,400 255,400"/>
    </g>
    <text class="brand-name" x="256" y="322" font-size="52" textLength="238" lengthAdjust="spacingAndGlyphs">VERDANO</text>
    <text class="phone phone--green" x="607" y="254" font-size="24" textLength="165" lengthAdjust="spacingAndGlyphs" transform="rotate(-3 607 254)">406-315-7084</text>
    <text class="services services--dark" x="517" y="288" transform="rotate(-4 517 288)" textLength="365" lengthAdjust="spacingAndGlyphs">WEEKLY LAWN MAINTENANCE   SPRINKLER REPAIRS   FERTILIZING   WEED CONTROL</text>
  </g>
</svg>
</body>
</html>
```